Banner Design for High End Jewelry Website

We need a banner for our website (brindlestone.com) for a sale that we will be running. The banner should be a size 1187 × 400. I have included a few pieces of jewelry to be included in the banner (do not need to use all, can use just some). The banner should say:
"Christmas is Closer Than You Think Sale!"
Shop Now

Industry/Entity Type

Jewelry

```html
<!DOCTYPE html>
<html lang="en">
<head>
<meta charset="utf-8">
<title>Brindlestone Christmas Sale Banner</title>
<link rel="stylesheet" href="https://fonts.googleapis.com/css2?family=Pinyon+Script&family=Libre+Baskerville&family=Lato:wght@700&display=swap">
<style>
  :root {
    --teal-deep: #0a2633;
    --teal-mid: #14495a;
    --teal-glow: #1f6578;
    --gold: #e2b83a;
    --gold-text: #e8bb3c;
    --gold-button: #d6b22a;
    --ink: #1c1a14;
    --jewel-gold: #c99a1e;
    --jewel-light: #f0cd55;
  }
  * { margin: 0; padding: 0; box-sizing: border-box; }
  html, body {
    width: 1200px;
    height: 404px;
    overflow: hidden;
    background: var(--teal-deep);
  }
  .banner {
    position: relative;
    width: 1200px;
    height: 404px;
    overflow: hidden;
    background:
      radial-gradient(ellipse 620px 360px at 560px 170px, var(--teal-glow) 0%, var(--teal-mid) 45%, var(--teal-deep) 100%);
  }
  .jewelry-visual {
    position: absolute;
    left: 42px;
    top: 52px;
    width: 575px;
    height: 300px;
    border-radius: 40px 120px 120px 40px;
    background:
      radial-gradient(ellipse 200px 140px at 150px 120px, rgba(90,140,110,0.55), transparent 70%),
      radial-gradient(ellipse 180px 150px at 440px 150px, var(--jewel-light), transparent 75%),
      linear-gradient(100deg, var(--jewel-gold) 0%, #b4861a 40%, var(--jewel-gold) 100%);
    opacity: 0.85;
  }
  .sale-message {
    position: absolute;
    left: 680px;
    top: 110px;
    width: 450px;
    text-align: center;
    color: var(--gold-text);
    font-family: "Libre Baskerville", "Times New Roman", serif;
    font-size: 33px;
    line-height: 48px;
  }
  .sale-message .script {
    font-family: "Pinyon Script", cursive;
    font-size: 52px;
    letter-spacing: 0.5px;
  }
  .divider {
    position: absolute;
    left: 855px;
    top: 243px;
    display: flex;
    gap: 30px;
  }
  .divider span {
    width: 12px;
    height: 12px;
    border-radius: 50%;
    background: var(--gold);
  }
  .shop-now {
    position: absolute;
    left: 841px;
    top: 306px;
    width: 142px;
    height: 43px;
    display: flex;
    align-items: center;
    justify-content: center;
    background: var(--gold-button);
    color: var(--ink);
    font-family: "Lato", Arial, sans-serif;
    font-weight: 700;
    font-size: 17px;
    letter-spacing: 0.3px;
    text-decoration: none;
  }
</style>
</head>
<body>
  <div class="banner">
    <div class="jewelry-visual" role="img" aria-label="Gold cocktail ring with cabochon gemstones and a diamond band beside a gold scale-textured cuff with pavé diamonds"></div>

    <h1 class="sale-message">
      <span class="script">Christmas</span> is closer than<br>you think sale!
    </h1>

    <div class="divider" aria-hidden="true"><span></span><span></span><span></span></div>

    <a class="shop-now" href="#">SHOP NOW</a>
  </div>
</body>
</html>
```